Want to go online this week, rush project, everything is there, just make it pretty

I need a pretty html5/css template for a already made site. Please do not rearrange anything unless you feel you can simplify the design. I have a raw site. Please play with the site by making an account with coupon code BRAMBLEPASS for free signup. Log in, log out, download as many designs as you can, then log in and log out. See everything cause it's brand new and I need it neat and pretty over the next few days if not sooner. So, after all that, the site is http://StitchloomPatternWorks.example
Updates

Project Deadline Extended
Reason: Extending until the 30th to give more time.

Is anyone working on something to submit? If you have something please submit asap as I will be closing this Sat night or Sunday morning

Industry/Entity Type

Online

Coding

Coded - Design and coding required

```html
<!DOCTYPE html>
<html lang="en">
<head>
<meta charset="utf-8">
<title>StitchloomPatternWorks – Muscle Cars 2</title>
<link href="https://fonts.googleapis.com/css2?family=Fira+Sans:wght@400;500;700;800&display=swap" rel="stylesheet">
<style>
:root{
  --page:#d6d6d6;
  --white:#ffffff;
  --ink:#222222;
  --muted:#555555;
  --green:#7aab3a;
  --green-dark:#5e8c28;
  --green-light:#bde08c;
  --green-text:#6ea12e;
  --card-foot:#ebebeb;
  --border:#a9a9a9;
  --btn-grey:#c9c9c9;
}
*{box-sizing:border-box;margin:0;padding:0}
html,body{width:901px;height:1200px;overflow:hidden}
body{background:var(--page);font-family:"Fira Sans",Arial,sans-serif;color:var(--ink);position:relative}
a{color:inherit;text-decoration:none}

.site-header{position:absolute;left:0;top:0;width:901px;height:153px;background:var(--white)}
.top-links{position:absolute;right:64px;top:10px;font-size:12px;color:var(--ink)}
.top-links a{padding:0 3px}
.brand{position:absolute;left:100px;top:48px;display:flex;align-items:center;gap:8px}
.brand-dot{width:14px;height:14px;border-radius:50%;background:var(--green)}
.brand-name{font-size:19px;font-weight:700;color:var(--green-dark);line-height:1.05}
.stats{position:absolute;left:330px;top:63px;width:240px;text-align:center;color:var(--green-text);font-size:14px;line-height:17px}
.stats b{font-weight:800}
.notify{position:absolute;left:612px;top:58px;width:205px}
.notify-email{display:block;width:205px;height:21px;border:1px solid #c8c8c8;border-radius:4px;background:#f4f4f4;font:italic 12px "Fira Sans",sans-serif;color:#666;padding:3px 14px}
.notify-btn{display:block;margin:6px 0 0 16px;width:174px;height:32px;border-radius:3px;background:linear-gradient(#86b54c,#5f8f2b);color:#fff;font-size:12px;text-align:center;line-height:32px;box-shadow:0 2px 2px rgba(0,0,0,.35)}

.main-nav{position:absolute;left:0;top:153px;width:901px;height:58px;display:flex;border-bottom:1px solid #9cbf70}
.nav-item{background:var(--green-light);text-align:center;padding-top:8px}
.nav-item strong{display:block;font-size:21px;font-weight:800;color:#333;line-height:24px}
.nav-item span{display:block;font-size:10px;color:#333;margin-top:3px}
.nav-item--active{background:var(--green)}
.nav-item--active strong,.nav-item--active span{color:#fff}

.pager{position:absolute;left:375px;width:462px;height:25px}
.pager-goto{position:absolute;left:0;top:2px;font-size:17px;font-weight:700;color:#333}
.pager-input{position:absolute;left:50px;top:0;width:63px;height:23px;border:1px solid #bbb;border-radius:3px;background:#fff;font-size:13px;color:#bbb;padding:3px 7px}
.pager-btn{position:absolute;top:0;height:25px;width:66px;border:1px solid #a8a8a8;border-radius:3px;background:var(--btn-grey);color:#777;font-size:14px;text-align:center;line-height:23px}
.pager-prev{left:232px}
.pager-next{left:396px}
.pager-pages{position:absolute;left:305px;top:1px;display:flex}
.pager-pages span{width:21px;height:23px;background:var(--btn-grey);color:#777;font-size:13px;text-align:center;line-height:23px}
.pager-pages .is-current{background:var(--green-light);color:#555}

.design-card{position:absolute;width:236px;height:339px;background:var(--card-foot);border:1px solid var(--border);border-radius:3px;box-shadow:0 1px 2px rgba(0,0,0,.25);overflow:hidden;text-align:center}
.card-top{height:194px;background:var(--white);position:relative}
.card-photo{position:absolute;left:7px;top:6px;width:220px;height:172px;background:radial-gradient(ellipse at 55% 50%,#7b4aa6 0 26%,#d8d2de 34%,#f3f3f3 60%)}
.card-title{position:absolute;left:0;right:0;top:163px;font-size:19px;font-weight:700;color:#222}
.card-count{margin-top:4px;font-size:12px;font-weight:700;color:#555}
.card-hoop{font-size:9px;color:#333;margin-top:1px}
.view-btn{display:flex;align-items:center;justify-content:center;gap:8px;margin:6px auto 0;width:88px;height:24px;border-radius:3px;background:linear-gradient(#8abd52,#5f8f2b);color:#fff;font-size:11px;box-shadow:0 2px 2px rgba(0,0,0,.3)}
.card-download{font-size:9px;color:#333;margin-top:12px;line-height:11px}
.formats{font-size:9px;color:#333;line-height:10px}
.formats a{color:var(--green-text)}
.card-meta{font-size:9px;color:#333;margin-top:14px}
.card-meta b{color:var(--green-text);font-weight:700}
.card-meta + .card-meta{margin-top:7px}

.site-footer{position:absolute;left:0;top:1141px;width:901px;text-align:center;font-size:9px;color:#333;line-height:10px}
</style>
</head>
<body>
<header class="site-header">
  <nav class="top-links"><a>Home</a>| <a>Register</a>| <a>Account</a>| <a>Contact</a>| <a>Search</a>| <a>Bookmark This Page</a></nav>
  <div class="brand"><span class="brand-dot"></span><span class="brand-name">Stitchloom<br>PatternWorks</span></div>
  <p class="stats"><b>27,906</b> unique designs online<br><b>1,982</b> design sets/packs</p>
  <form class="notify"><span class="notify-email">Email</span><span class="notify-btn">Get notified of new designs!</span></form>
</header>

<nav class="main-nav">
  <a class="nav-item" style="width:334px"><strong>FREE</strong><span>Get your today's free design</span></a>
  <a class="nav-item nav-item--active" style="width:235px"><strong>Register</strong><span>for unlimited embroidery design downloads!</span></a>
  <a class="nav-item" style="width:332px"><strong>DVD</strong><span>Get all Designs on DVD | coming soon</span></a>
</nav>

<div class="pager" style="top:253px">
  <span class="pager-goto">Go to</span><span class="pager-input">Page</span>
  <a class="pager-btn pager-prev">Prev</a>
  <div class="pager-pages"><span>1</span><span>2</span><span class="is-current">3</span><span>4</span></div>
  <a class="pager-btn pager-next">Next</a>
</div>

<main>
<article class="design-card" style="left:66px;top:292px">
  <div class="card-top"><div class="card-photo" role="img" aria-label="Embroidered purple muscle car"></div><h2 class="card-title">Muscle Cars 2</h2></div>
  <p class="card-count">10 Designs</p><p class="card-hoop">All Fit the 4X4 Hoop</p>
  <a class="view-btn"><svg width="14" height="14" viewBox="0 0 14 14"><circle cx="8" cy="6" r="4" fill="none" stroke="#fff" stroke-width="2"/><line x1="5" y1="9" x2="1" y2="13" stroke="#fff" stroke-width="2.5"/></svg>view set</a>
  <p class="card-download">Download now, select your format:</p>
  <p class="formats">[ <a>art</a> ][ <a>dst</a> ][ <a>exp</a> ][ <a>hus</a> ][ <a>jef</a> ]</p>
  <p class="formats">[ <a>pcs</a> ][ <a>pes</a> ][ <a>sew</a> ][ <a>vip</a> ][ <a>xxx</a> ]</p>
  <p class="card-meta">Categories: <b>Filled Design, Cars</b></p>
  <p class="card-meta">Added/Updated: <b>October 21, 2014</b></p>
</article>
<article class="design-card" style="left:334px;top:292px">
  <div class="card-top"><div class="card-photo" role="img" aria-label="Embroidered purple muscle car"></div><h2 class="card-title">Muscle Cars 2</h2></div>
  <p class="card-count">10 Designs</p><p class="card-hoop">All Fit the 4X4 Hoop</p>
  <a class="view-btn"><svg width="14" height="14" viewBox="0 0 14 14"><circle cx="8" cy="6" r="4" fill="none" stroke="#fff" stroke-width="2"/><line x1="5" y1="9" x2="1" y2="13" stroke="#fff" stroke-width="2.5"/></svg>view set</a>
  <p class="card-download">Download now, select your format:</p>
  <p class="formats">[ <a>art</a> ][ <a>dst</a> ][ <a>exp</a> ][ <a>hus</a> ][ <a>jef</a> ]</p>
  <p class="formats">[ <a>pcs</a> ][ <a>pes</a> ][ <a>sew</a> ][ <a>vip</a> ][ <a>xxx</a> ]</p>
  <p class="card-meta">Categories: <b>Filled Design, Cars</b></p>
  <p class="card-meta">Added/Updated: <b>October 21, 2014</b></p>
</article>
<article class="design-card" style="left:602px;top:292px">
  <div class="card-top"><div class="card-photo" role="img" aria-label="Embroidered purple muscle car"></div><h2 class="card-title">Muscle Cars 2</h2></div>
  <p class="card-count">10 Designs</p><p class="card-hoop">All Fit the 4X4 Hoop</p>
  <a class="view-btn"><svg width="14" height="14" viewBox="0 0 14 14"><circle cx="8" cy="6" r="4" fill="none" stroke="#fff" stroke-width="2"/><line x1="5" y1="9" x2="1" y2="13" stroke="#fff" stroke-width="2.5"/></svg>view set</a>
  <p class="card-download">Download now, select your format:</p>
  <p class="formats">[ <a>art</a> ][ <a>dst</a> ][ <a>exp</a> ][ <a>hus</a> ][ <a>jef</a> ]</p>
  <p class="formats">[ <a>pcs</a> ][ <a>pes</a> ][ <a>sew</a> ][ <a>vip</a> ][ <a>xxx</a> ]</p>
  <p class="card-meta">Categories: <b>Filled Design, Cars</b></p>
  <p class="card-meta">Added/Updated: <b>October 21, 2014</b></p>
</article>
<article class="design-card" style="left:66px;top:662px">
  <div class="card-top"><div class="card-photo" role="img" aria-label="Embroidered purple muscle car"></div><h2 class="card-title">Muscle Cars 2</h2></div>
  <p class="card-count">10 Designs</p><p class="card-hoop">All Fit the 4X4 Hoop</p>
  <a class="view-btn"><svg width="14" height="14" viewBox="0 0 14 14"><circle cx="8" cy="6" r="4" fill="none" stroke="#fff" stroke-width="2"/><line x1="5" y1="9" x2="1" y2="13" stroke="#fff" stroke-width="2.5"/></svg>view set</a>
  <p class="card-download">Download now, select your format:</p>
  <p class="formats">[ <a>art</a> ][ <a>dst</a> ][ <a>exp</a> ][ <a>hus</a> ][ <a>jef</a> ]</p>
  <p class="formats">[ <a>pcs</a> ][ <a>pes</a> ][ <a>sew</a> ][ <a>vip</a> ][ <a>xxx</a> ]</p>
  <p class="card-meta">Categories: <b>Filled Design, Cars</b></p>
  <p class="card-meta">Added/Updated: <b>October 21, 2014</b></p>
</article>
<article class="design-card" style="left:334px;top:662px">
  <div class="card-top"><div class="card-photo" role="img" aria-label="Embroidered purple muscle car"></div><h2 class="card-title">Muscle Cars 2</h2></div>
  <p class="card-count">10 Designs</p><p class="card-hoop">All Fit the 4X4 Hoop</p>
  <a class="view-btn"><svg width="14" height="14" viewBox="0 0 14 14"><circle cx="8" cy="6" r="4" fill="none" stroke="#fff" stroke-width="2"/><line x1="5" y1="9" x2="1" y2="13" stroke="#fff" stroke-width="2.5"/></svg>view set</a>
  <p class="card-download">Download now, select your format:</p>
  <p class="formats">[ <a>art</a> ][ <a>dst</a> ][ <a>exp</a> ][ <a>hus</a> ][ <a>jef</a> ]</p>
  <p class="formats">[ <a>pcs</a> ][ <a>pes</a> ][ <a>sew</a> ][ <a>vip</a> ][ <a>xxx</a> ]</p>
  <p class="card-meta">Categories: <b>Filled Design, Cars</b></p>
  <p class="card-meta">Added/Updated: <b>October 21, 2014</b></p>
</article>
<article class="design-card" style="left:602px;top:662px">
  <div class="card-top"><div class="card-photo" role="img" aria-label="Embroidered purple muscle car"></div><h2 class="card-title">Muscle Cars 2</h2></div>
  <p class="card-count">10 Designs</p><p class="card-hoop">All Fit the 4X4 Hoop</p>
  <a class="view-btn"><svg width="14" height="14" viewBox="0 0 14 14"><circle cx="8" cy="6" r="4" fill="none" stroke="#fff" stroke-width="2"/><line x1="5" y1="9" x2="1" y2="13" stroke="#fff" stroke-width="2.5"/></svg>view set</a>
  <p class="card-download">Download now, select your format:</p>
  <p class="formats">[ <a>art</a> ][ <a>dst</a> ][ <a>exp</a> ][ <a>hus</a> ][ <a>jef</a> ]</p>
  <p class="formats">[ <a>pcs</a> ][ <a>pes</a> ][ <a>sew</a> ][ <a>vip</a> ][ <a>xxx</a> ]</p>
  <p class="card-meta">Categories: <b>Filled Design, Cars</b></p>
  <p class="card-meta">Added/Updated: <b>October 21, 2014</b></p>
</article>
</main>

<div class="pager" style="top:1022px">
  <span class="pager-goto">Go to</span><span class="pager-input">Page</span>
  <a class="pager-btn pager-prev">Prev</a>
  <div class="pager-pages"><span>1</span><span>2</span><span class="is-current">3</span><span>4</span></div>
  <a class="pager-btn pager-next">Next</a>
</div>

<footer class="site-footer">
  <p>Website and Embroidery Designs Copyright (C) Harlow Reed Systems Inc.</p>
  <p>Permission granted to use machine embroidery designs for your own commercial and personal embroidery.</p>
  <p>Permission denied to resell or give away machine embroidery designs in electronic format.</p>
</footer>
</body>
</html>
```